Salon and Spa Distributor Business Card

Need a business card. We are are distributor in the salon and spa industry. We identify with natural beauty. Need a card with:
Company Name: Petal Harbor"
Title: "President & CEO"
Address
Company Phone number
email
website
Tag Line:" The Professional Salon Source"

Industry/Entity Type

Business

Contact Information for Business Card

Name: Leo Mendoza
Title: "President & CEO"
Address: 317 Birchline Ave, Westbrook, NJ 08412
Company Phone number: 800-463-5108
email: leomendoza@petalharbor-example.com
website: www.petalharbor-example.com

Requirements
Should not have
• No black backgrounds

```html
<!DOCTYPE html>
<html lang="en">
<head>
<meta charset="utf-8">
<title>Petal Harbor Business Card</title>
<link href="https://fonts.googleapis.com/css2?family=Roboto:wght@400;500;700&display=swap" rel="stylesheet">
<style>
  :root {
    --backdrop: #ece9e4;
    --card: #f9f9f8;
    --brand-green: #4f9e3a;
    --mark-green: #6cbf45;
    --ink: #161b2b;
    --ink-soft: #2a2d36;
    --band-1: #d66c4d;
    --band-2: #e0b02f;
    --band-3: #d9d66b;
    --band-4: #a2c650;
    --band-5: #8ccfd9;
    --band-6: #6ea5d5;
    --band-7: #9c8dc7;
  }
  * { margin: 0; padding: 0; box-sizing: border-box; }
  html, body {
    width: 1200px; height: 812px; overflow: hidden;
    background: var(--backdrop);
    font-family: "Roboto", Arial, sans-serif;
  }
  .sheet { position: relative; width: 1200px; height: 812px; }
  .card {
    position: absolute; top: 257px;
    width: 520px; height: 297px;
    background: var(--card);
    box-shadow: 0 6px 18px rgba(0,0,0,0.12);
    overflow: hidden;
  }
  .card--front { left: 50px; }
  .card--back { left: 630px; }

  .brand { position: absolute; display: flex; align-items: center; }
  .brand__dot { flex: none; border-radius: 50%; background: var(--mark-green); }
  .brand__text { display: flex; flex-direction: column; }
  .brand__name { color: var(--brand-green); font-weight: 400; white-space: nowrap; line-height: 1.1; }
  .brand__tagline { color: var(--ink-soft); font-weight: 400; white-space: nowrap; line-height: 1.2; }

  .card--front .brand { top: 26px; left: 50%; transform: translateX(-50%); gap: 10px; }
  .card--front .brand__dot { width: 42px; height: 42px; }
  .card--front .brand__name { font-size: 21px; }
  .card--front .brand__tagline { font-size: 11px; margin-top: 2px; }

  .holder { position: absolute; top: 98px; left: 0; right: 0; text-align: center; }
  .holder__name { font-size: 34px; font-weight: 700; color: var(--ink); letter-spacing: -0.3px; line-height: 1.15; }
  .holder__title { font-size: 14px; font-weight: 500; color: var(--ink-soft); margin-top: 4px; }

  .contact { position: absolute; font-size: 13px; font-weight: 500; color: var(--ink-soft); line-height: 18px; }
  .contact--left { left: 30px; bottom: 46px; }
  .contact--right { right: 26px; bottom: 64px; text-align: right; }

  .band { position: absolute; left: 0; right: 0; bottom: 0; height: 24px; display: flex; }
  .band span { flex: 1; }
  .band span:nth-child(1) { background: var(--band-1); }
  .band span:nth-child(2) { background: var(--band-2); }
  .band span:nth-child(3) { background: var(--band-3); }
  .band span:nth-child(4) { background: var(--band-4); }
  .band span:nth-child(5) { background: var(--band-5); }
  .band span:nth-child(6) { background: var(--band-6); }
  .band span:nth-child(7) { background: var(--band-7); }

  .card--back .brand { top: 50%; left: 50%; transform: translate(-50%, -62%); gap: 18px; }
  .card--back .brand__dot { width: 86px; height: 86px; }
  .card--back .brand__name { font-size: 36px; }
  .card--back .brand__tagline { font-size: 15px; margin-top: 6px; }
</style>
</head>
<body>
<main class="sheet">
  <section class="card card--front" aria-label="Business card front">
    <div class="brand">
      <span class="brand__dot"></span>
      <div class="brand__text">
        <span class="brand__name">Petal Harbor</span>
        <span class="brand__tagline">The Professional Salon Source</span>
      </div>
    </div>
    <div class="holder">
      <h1 class="holder__name">Leo Mendoza</h1>
      <p class="holder__title">President &amp; CEO</p>
    </div>
    <div class="contact contact--right">
      <p>leomendoza@petalharbor-example.com</p>
      <p>www.petalharbor-example.com</p>
    </div>
    <div class="contact contact--left">
      <p>800-463-5108</p>
      <p>317 Birchline Ave, Westbrook, NJ 08412</p>
    </div>
    <div class="band"><span></span><span></span><span></span><span></span><span></span><span></span><span></span></div>
  </section>

  <section class="card card--back" aria-label="Business card back">
    <div class="brand">
      <span class="brand__dot"></span>
      <div class="brand__text">
        <span class="brand__name">Petal Harbor</span>
        <span class="brand__tagline">The Professional Salon Source</span>
      </div>
    </div>
    <div class="band"><span></span><span></span><span></span><span></span><span></span><span></span><span></span></div>
  </section>
</main>
</body>
</html>
```